Business card design needed

I need a business card for my Sydney Painting Business, that specialises in painting High -end residential homes. i want the design to look clean, modern and edgy. i also want a logo next to the RL Decorating, using RLD together.

Industry/Entity Type

Residential

Contact Information for Business Card

RL Decorating (business name),LIC 871536K, Rob Lindqvist, robert.lindqvist@brushmail.example, mobile 0419352807

```html
<!DOCTYPE html>
<html lang="en">
<head>
<meta charset="utf-8">
<title>RL Decorating – Business Card</title>
<link rel="stylesheet" href="https://fonts.googleapis.com/css2?family=Lexend+Exa:wght@400;500&family=Raleway:wght@400;500&display=swap">
<style>
  :root {
    --page-bg: #ffffff;
    --card-black: #000000;
    --card-glow: #1c1c1c;
    --brand-blue: #2f86f6;
    --mark-blue: #2a8cff;
    --wordmark-grey: #a7a9ac;
    --text-white: #f2f2f2;
  }
  * { box-sizing: border-box; margin: 0; padding: 0; }
  html, body {
    width: 1200px;
    height: 883px;
    overflow: hidden;
    background: var(--page-bg);
  }
  .business-card {
    position: absolute;
    left: 80px;
    top: 141px;
    width: 1040px;
    height: 600px;
    background: linear-gradient(to bottom, var(--card-black) 0%, var(--card-black) 78%, var(--card-glow) 100%);
    color: var(--text-white);
    font-family: "Raleway", sans-serif;
  }
  .brand-logo {
    position: absolute;
    left: 0;
    right: 0;
    top: 109px;
    display: flex;
    flex-direction: column;
    align-items: center;
  }
  .brand-square {
    width: 150px;
    height: 150px;
    background: var(--mark-blue);
  }
  .brand-name {
    margin-top: 30px;
    font-family: "Lexend Exa", sans-serif;
    font-weight: 400;
    font-size: 32px;
    letter-spacing: 3px;
    text-transform: uppercase;
    color: var(--wordmark-grey);
  }
  .person {
    position: absolute;
    left: 40px;
    top: 440px;
  }
  .person-name {
    font-family: "Lexend Exa", sans-serif;
    font-weight: 500;
    font-size: 33px;
    letter-spacing: 0.5px;
    color: var(--brand-blue);
    line-height: 1.1;
  }
  .person-role {
    margin-top: 4px;
    font-family: "Lexend Exa", sans-serif;
    font-size: 24px;
    letter-spacing: 2px;
    color: var(--text-white);
  }
  .contact-details {
    position: absolute;
    right: 43px;
    top: 442px;
    text-align: right;
    list-style: none;
    font-size: 27px;
    line-height: 37px;
  }
  .contact-label {
    color: var(--brand-blue);
    margin-right: 4px;
  }
</style>
</head>
<body>
  <main class="business-card">
    <div class="brand-logo">
      <div class="brand-square" aria-hidden="true"></div>
      <div class="brand-name">RL Decorating</div>
    </div>

    <div class="person">
      <p class="person-name">Rob Lindqvist</p>
      <p class="person-role">PAINTER</p>
    </div>

    <ul class="contact-details">
      <li>RL Decorating, LIC 871536K</li>
      <li><span class="contact-label">E</span>robert.lindqvist@brushmail.example</li>
      <li><span class="contact-label">M</span>041 935 2807</li>
    </ul>
  </main>
</body>
</html>
```